Next-Gen B2B Sales Negotiation App - UI Design for iOS

Develop a user-friendly dark-mode interface for a B2B sales negotiation assistant app for a company called Quorvel. The UI will showcase a single screen with features like counterparty search, agenda selection, and email drafting. Design should reflect a functional iOS app with realistic placeholder data to create a genuine experience.

Precise task description in attachment.

Target Market(s)

B2B

Requirements
Must have
• Each UI picture should look like a screen capture of an iphone
Nice to have
• The UI designs need to show the navigation and the app in use

```html
<!DOCTYPE html>
<html lang="en">
<head>
<meta charset="utf-8">
<title>Quorvel – Negotiation Assistant</title>
<link href="https://fonts.googleapis.com/css2?family=Pixelify+Sans:wght@400;500;600&display=swap" rel="stylesheet">
<style>
:root{
  --page:#ffffff;
  --screen-top:#2b0d36;
  --screen:#0e0a13;
  --card:#150f1b;
  --card-line:#221a2b;
  --row:#1b1421;
  --icon:#4f2a6b;
  --text:#f1ecf5;
  --muted:#6e6378;
  --pink:#ff3f93;
  --cyan:#2fd6ee;
  --magenta:#e02fd0;
  --violet:#8a5cff;
  --btn-text:#c7bfcd;
}
*{box-sizing:border-box;margin:0;padding:0}
html,body{width:735px;height:1200px;overflow:hidden;background:var(--page)}
body{font-family:"Pixelify Sans",monospace;color:var(--text);text-transform:uppercase}
.stage{position:relative;width:735px;height:1200px}
.screen{
  position:absolute;left:50%;top:15px;width:331px;height:1235px;
  margin-left:-165.5px;transform:scale(.947);transform-origin:top center;
  border-radius:22px;overflow:hidden;
  background:linear-gradient(180deg,var(--screen-top) 0,#190a20 120px,var(--screen) 260px,var(--screen) 100%);
}
.app-header{position:absolute;top:22px;left:12px;right:12px;height:36px;display:flex;align-items:center;justify-content:space-between}
.menu-btn{width:34px;height:34px;border-radius:50%;background:#2a1a36;display:flex;align-items:center;justify-content:center}
.brand{font-size:32px;font-weight:500;text-transform:none;letter-spacing:1px;color:var(--text)}
.avatar{width:34px;height:34px;border-radius:50%;background:radial-gradient(circle at 50% 40%,#d7c2b0,#6d5a55 70%);border:2px solid #e8e3ea}
.card{position:absolute;left:18px;width:302px;background:var(--card);border:1px solid var(--card-line);border-radius:12px;overflow:hidden}
.card-title{text-align:center;font-size:13px;font-weight:500;height:42px;line-height:42px;letter-spacing:.5px}
.c{color:var(--cyan)}.m{color:var(--magenta)}.v{color:var(--violet)}
.field{height:56px;background:var(--row);display:flex;align-items:center;padding:0 16px;margin-bottom:12px;border-top:1px solid #241b2c}
.field:last-child{margin-bottom:0}
.field svg.ico{width:22px;height:22px;flex:none}
.field-text{margin-left:15px;flex:1}
.label{font-size:8px;font-weight:400;color:var(--muted);letter-spacing:.3px}
.value{font-size:11px;font-weight:500;margin-top:4px;letter-spacing:.3px}
.trail{width:18px;height:18px;border-radius:50%;background:#231b2a;display:flex;align-items:center;justify-content:center}
.mode{display:flex;gap:14px;padding:0 15px;margin:0 0 12px}
.mode-btn{flex:1;height:45px;border-radius:5px;display:flex;align-items:center;padding-left:12px;gap:14px;font-size:11px;font-weight:500;border:1px solid #241b2c;background:#130e18}
.mode-btn.active{background:var(--pink);border-color:var(--pink)}
.contacts{display:flex;gap:13px;padding:4px 13px 0 15px}
.contact{width:83px;height:72px;border-radius:5px;border:1px solid #241b2c;background:#130e18;display:flex;flex-direction:column;align-items:center;justify-content:center;gap:10px;font-size:11px;font-weight:500;color:var(--btn-text)}
.contact.active{background:var(--pink);border-color:var(--pink);color:#fff}
.draft{background:var(--row);border-top:1px solid #241b2c;padding:16px 18px 18px 14px;display:flex;gap:14px;height:155px}
.draft p{font-size:11px;font-weight:500;line-height:20.5px;letter-spacing:.2px}
.actions{position:absolute;left:18px;right:11px;top:1105px;display:flex;justify-content:space-between}
.btn{width:140px;height:45px;border-radius:10px;display:flex;align-items:center;justify-content:center;font-size:12px;font-weight:500}
.btn.primary{background:var(--pink);color:#fff}
.btn.ghost{border:1px solid #2c2434;color:var(--btn-text)}
</style>
</head>
<body>
<div class="stage">
  <main class="screen">
    <header class="app-header">
      <div class="menu-btn"><svg width="14" height="12" viewBox="0 0 14 12"><rect x="1" y="1" width="11" height="2" fill="#d93fd0"/><rect x="1" y="5" width="7" height="2" fill="#d93fd0"/><rect x="1" y="9" width="11" height="2" fill="#d93fd0"/></svg></div>
      <div class="brand">quorvel</div>
      <div class="avatar" role="img" aria-label="User profile photo"></div>
    </header>

    <section class="card" style="top:92px">
      <h2 class="card-title"><span class="c">Please</span> <span class="m">Select</span></h2>
      <div class="field">
        <svg class="ico" viewBox="0 0 22 22"><rect x="2" y="5" width="9" height="15" fill="var(--icon)"/><rect x="11" y="10" width="8" height="10" fill="var(--icon)"/></svg>
        <div class="field-text"><div class="label">Please select</div><div class="value">Company</div></div>
        <div class="trail"><svg width="8" height="5" viewBox="0 0 8 5"><path d="M1 1l3 3 3-3" stroke="#5e5366" fill="none"/></svg></div>
      </div>
      <div class="field">
        <svg class="ico" viewBox="0 0 22 22"><rect x="3" y="3" width="10" height="17" fill="var(--icon)"/><rect x="13" y="9" width="6" height="11" fill="var(--icon)"/><rect x="6" y="7" width="4" height="2" fill="#1b1421"/><rect x="6" y="11" width="4" height="2" fill="#1b1421"/></svg>
        <div class="field-text"><div class="label">Select company name</div><div class="value">Brindlewood Works</div></div>
        <div class="trail"><svg width="8" height="5" viewBox="0 0 8 5"><path d="M1 1l3 3 3-3" stroke="#5e5366" fill="none"/></svg></div>
      </div>
      <div class="field">
        <svg class="ico" viewBox="0 0 22 22"><circle cx="11" cy="7" r="4.5" fill="var(--icon)"/><path d="M2 20c0-5 4-8 9-8s9 3 9 8z" fill="var(--icon)"/></svg>
        <div class="field-text"><div class="label">Select your position</div><div class="value">CEO</div></div>
        <div class="trail"><svg width="8" height="5" viewBox="0 0 8 5"><path d="M1 1l3 3 3-3" stroke="#5e5366" fill="none"/></svg></div>
      </div>
    </section>

    <section class="card" style="top:344px">
      <h2 class="card-title"><span class="c">Agen</span><span class="m">da</span></h2>
      <div class="field">
        <svg class="ico" viewBox="0 0 22 22"><rect x="4" y="4" width="14" height="16" rx="2" fill="var(--icon)"/><rect x="8" y="2" width="6" height="4" fill="var(--icon)"/><rect x="7" y="10" width="8" height="1.5" fill="#1b1421"/><rect x="7" y="14" width="8" height="1.5" fill="#1b1421"/></svg>
        <div class="field-text"><div class="label">Select agenda</div><div class="value">Book a meeting</div></div>
        <div class="trail"><svg width="8" height="5" viewBox="0 0 8 5"><path d="M1 1l3 3 3-3" stroke="#5e5366" fill="none"/></svg></div>
      </div>
      <div class="field">
        <svg class="ico" viewBox="0 0 22 22"><circle cx="9" cy="10" r="8" fill="var(--icon)"/><rect x="12" y="12" width="9" height="8" rx="1" fill="#6b3a8f"/></svg>
        <div class="field-text"><div class="label">Describe meeting duration</div><div class="value">30 minutes</div></div>
        <div class="trail"><svg width="10" height="10" viewBox="0 0 10 10"><circle cx="5" cy="5" r="4.5" fill="#5e5366"/><path d="M5 2.5V5l1.6 1" stroke="#1b1421" fill="none"/></svg></div>
      </div>
      <div class="field">
        <svg class="ico" viewBox="0 0 22 22"><rect x="2" y="4" width="18" height="16" rx="2" fill="var(--icon)"/><rect x="2" y="4" width="18" height="4" fill="#6b3a8f"/></svg>
        <div class="field-text"><div class="label">Date</div><div class="value">February 17, 2025</div></div>
        <div class="trail"><svg width="10" height="10" viewBox="0 0 10 10"><rect x="1" y="2" width="8" height="7" fill="#5e5366"/></svg></div>
      </div>
      <div class="mode">
        <div class="mode-btn active">
          <svg width="24" height="22" viewBox="0 0 24 22"><rect x="2" y="2" width="11" height="18" rx="2" fill="none" stroke="#fff" stroke-width="1.6"/><rect x="14" y="2" width="8" height="7" rx="1" fill="#fff"/><circle cx="7.5" cy="12" r="2.5" fill="#fff"/></svg>Online
        </div>
        <div class="mode-btn">
          <svg width="26" height="22" viewBox="0 0 26 22"><circle cx="13" cy="6" r="4" fill="var(--icon)"/><rect x="3" y="12" width="20" height="8" fill="var(--icon)"/><circle cx="4" cy="10" r="2.5" fill="var(--icon)"/><circle cx="22" cy="10" r="2.5" fill="var(--icon)"/></svg>On-site
        </div>
      </div>
      <div class="field" style="padding-left:12px">
        <svg class="ico" viewBox="0 0 22 22"><rect x="2" y="4" width="18" height="16" rx="2" fill="var(--icon)"/><rect x="2" y="4" width="18" height="4" fill="#6b3a8f"/></svg>
        <div class="field-text"><div class="label">Describe selling points</div><div class="value">We can save your time</div></div>
      </div>
    </section>

    <section class="card" style="top:722px;height:136px">
      <h2 class="card-title" style="height:38px;line-height:40px"><span class="c">Contact</span> <span class="m">Method</span></h2>
      <div class="contacts">
        <div class="contact active"><svg width="26" height="18" viewBox="0 0 26 18"><rect x="1" y="1" width="24" height="16" rx="2" fill="#fff"/><path d="M2 2l11 8 11-8" stroke="var(--pink)" stroke-width="2" fill="none"/></svg>Email</div>
        <div class="contact"><svg width="22" height="22" viewBox="0 0 22 22"><rect x="1" y="1" width="20" height="20" rx="2" fill="var(--icon)"/></svg>ProNet</div>
        <div class="contact"><svg width="16" height="24" viewBox="0 0 16 24"><rect x="1" y="1" width="14" height="22" rx="2" fill="var(--icon)"/><circle cx="8" cy="19" r="1.2" fill="#130e18"/></svg>Phone</div>
      </div>
    </section>

    <section class="card" style="top:878px;height:198px">
      <h2 class="card-title"><span class="c">Email</span> <span class="v">Draf</span><span class="m">ting</span></h2>
      <div class="draft">
        <svg width="20" height="20" viewBox="0 0 20 20" style="flex:none;margin-top:2px"><rect x="1" y="1" width="14" height="17" rx="2" fill="var(--icon)"/><path d="M9 15l9-9" stroke="#8a5ca8" stroke-width="3"/><rect x="4" y="5" width="7" height="1.5" fill="#1b1421"/><rect x="4" y="9" width="5" height="1.5" fill="#1b1421"/></svg>
        <p>Hi Marek, I am reaching out to you as I have a solution to save your money and time. I am kindly proposing a meeting for week 8, for instance on Monday 17 February.<br>Best regards, Elias</p>
      </div>
    </section>

    <div class="actions">
      <div class="btn primary">Send now</div>
      <div class="btn ghost">Schedule</div>
    </div>
  </main>
</div>
</body>
</html>
```